Wedding Invitation for a wedding at home - personal, romantic event

Want a wedding invitation that is to be printed onto card.
Size to be 148mm x 210mm
For it to open like a book not tent card
Have a picture of a house that I want to be the front cover.
I've attached 2 pictures. I like the picture without the man but with the grass
For the photo to become a drawing and the colours to be brighter.
If you could use the picture of us and get us in one of the windows.
If you could put the picture of the dog maybe somewhere on the grass.
Love the colour of the sky in the picture of the beach

Words to be on the inside of the card:
Together with our families
You are invited to the Wedding Reception of Polly Faraway and Ned Bramwick
On Saturday 9th of September 2017 at 6pm
At Bramwick's Keep, 41b, Fennow Crescent, Camberley, Surrey, GU19 7QX
Carriages at 1am
RSVP by Friday 27th of July to 07712 958 061

Words on the Back page:
With all that we have, we've been truly blessed.
Your presence and prayers are all that we request.
But if you desire to give nonetheless,
Monetary gift is one we suggest.

If the pages can be white.
Writing in gold
gold border on all pages

Target Market(s)

Wedding guests

Industry/Entity Type

Wedding

Font styles to use
Script

Requirements
Must have
• Romantic feel. Our wedding colours are white, gold and rose gold.
• Designer to be creative and I do not have much inspiration.
Nice to have
• metallic colours
• Maybe have MR & MRS in gold metallic on the front page

```html
<!DOCTYPE html>
<html lang="en">
<head>
<meta charset="utf-8">
<title>Wedding Invitation – Back Page Verse</title>
<link rel="stylesheet" href="https://fonts.googleapis.com/css2?family=Great+Vibes&display=swap">
<style>
  :root {
    --page-white: #ffffff;
    --verse-gold: #968a32;
  }
  html, body {
    margin: 0;
    padding: 0;
    width: 846px;
    height: 1200px;
    overflow: hidden;
    background: var(--page-white);
  }
  .back-page {
    position: relative;
    width: 846px;
    height: 1200px;
    background: var(--page-white);
  }
  .gift-verse {
    position: absolute;
    top: 302px;
    left: 0;
    width: 846px;
    margin: 0;
    text-align: center;
    font-family: "Great Vibes", cursive;
    font-size: 47px;
    line-height: 72px;
    color: var(--verse-gold);
  }
  .gift-verse span {
    display: block;
  }
</style>
</head>
<body>
  <main class="back-page">
    <p class="gift-verse">
      <span>With all that we have,</span>
      <span>we’ve been truly blessed.</span>
      <span>Your presence and prayers</span>
      <span>are all that we request.</span>
      <span>But if you desire</span>
      <span>to give nonetheless,</span>
      <span>Monetary gift</span>
      <span>is one we suggest.</span>
    </p>
  </main>
</body>
</html>
```